Tarnwick Bathrooms

Fix our flyer add as the one we got made has the wrong phone number on it would like different photos on it

Want it to Stand out and be in your face!

I will attach our logo
phone number is 0487652970
Email is Jory@tarnwickbathrooms.com.au

happy to keep all prices the same

If you can make it better happy to tip $$

```html
<!DOCTYPE html>
<html lang="en">
<head>
<meta charset="utf-8">
<title>Tarnwick Bathrooms – Flyer</title>
<link rel="stylesheet" href="https://fonts.googleapis.com/css2?family=Jost:wght@300;400;500;600;700&family=Poppins:wght@500;600;700;800&display=swap">
<style>
  :root {
    --blue: #1a6fbd;
    --panel-blue: #1469b5;
    --ink: #0d0d0d;
    --grey-band: #a6a8ab;
    --grey-panel: #bcbec1;
    --white: #ffffff;
  }
  * { margin: 0; padding: 0; box-sizing: border-box; }
  html, body { width: 935px; height: 1200px; overflow: hidden; background: var(--white); }
  .flyer { position: relative; width: 935px; height: 1200px; background: var(--white); font-family: "Poppins", sans-serif; color: var(--ink); }
  .abs { position: absolute; line-height: 1; white-space: nowrap; }

  /* brand */
  .brand-mark { left: 34px; top: 70px; width: 22px; height: 22px; background: var(--blue); }
  .brand-name { left: 66px; top: 62px; font-family: "Jost", sans-serif; font-weight: 500; font-size: 38px; color: var(--blue); letter-spacing: 1px; }
  .brand-sub { left: 66px; top: 106px; font-family: "Jost", sans-serif; font-weight: 500; font-size: 17px; color: var(--blue); letter-spacing: 9px; }

  /* intro */
  .region { left: 32px; top: 190px; font-family: "Jost", sans-serif; font-weight: 700; font-size: 44px; color: var(--blue); }
  .region-note { font-weight: 300; font-size: 30px; color: var(--ink); margin-left: 6px; }
  .family { left: 33px; top: 244px; font-family: "Jost", sans-serif; font-weight: 300; font-size: 30px; }
  .family strong { font-weight: 700; }

  .name-band { left: 0; top: 298px; width: 453px; height: 43px; background: var(--grey-band); }
  .name-band span { position: absolute; left: 33px; top: 9px; font-family: "Jost", sans-serif; font-weight: 600; font-size: 24px; line-height: 1; }

  .fully { left: 33px; top: 352px; font-family: "Jost", sans-serif; font-weight: 700; font-size: 30px; }
  .licensed { left: 31px; top: 388px; font-family: "Jost", sans-serif; font-weight: 600; font-size: 56px; color: var(--blue); letter-spacing: 4px; }
  .insured { left: 31px; top: 448px; font-family: "Jost", sans-serif; font-weight: 600; font-size: 56px; color: var(--blue); letter-spacing: 1px; }
  .insured .amp { color: var(--ink); margin-right: 8px; }

  /* hero */
  .hero-photo { left: 468px; top: 0; width: 467px; height: 618px; background: linear-gradient(100deg, #8a6a52 0%, #b79a83 35%, #d8d3cc 70%, #ece9e5 100%); }
  .bracket { position: absolute; background: var(--ink); border-radius: 14px; }

  /* packages */
  .save-tab { position: absolute; height: 36px; background: var(--ink); color: var(--white); font-family: "Poppins", sans-serif; font-weight: 700; font-size: 11px; letter-spacing: 0.3px; }
  .save-tab span { position: absolute; top: 12px; line-height: 1; }
  .pkg-photo { position: absolute; }
  .pkg-title { font-family: "Poppins", sans-serif; font-weight: 800; color: var(--blue); }
  .pkg-from { font-family: "Poppins", sans-serif; font-weight: 700; font-size: 11px; }
  .pkg-price { font-family: "Poppins", sans-serif; font-weight: 700; font-size: 25px; letter-spacing: 0.5px; }

  .terms { left: 102px; top: 1174px; font-family: "Poppins", sans-serif; font-weight: 400; font-size: 10.5px; }

  /* services */
  .services { position: absolute; left: 468px; top: 618px; width: 467px; height: 407px; background: var(--panel-blue); border-bottom-left-radius: 16px; color: var(--white); }
  .services-title { left: 49px; top: 14px; font-family: "Jost", sans-serif; font-weight: 600; font-size: 27px; }
  .services-sub { left: 49px; top: 53px; font-family: "Jost", sans-serif; font-weight: 300; font-size: 16px; }
  .service-list { position: absolute; left: 60px; top: 112px; list-style: none; }
  .service-list li { position: relative; height: 42.3px; padding-left: 35px; font-family: "Poppins", sans-serif; font-weight: 600; font-size: 25px; letter-spacing: 1.5px; line-height: 1; }
  .service-list li::before { content: ""; position: absolute; left: 3px; top: 8px; width: 10px; height: 10px; border: 2px solid var(--ink); transform: rotate(45deg); background: radial-gradient(var(--ink) 35%, transparent 40%); }
  .services-note { left: 43px; top: 369px; font-family: "Jost", sans-serif; font-weight: 300; font-size: 16.5px; }

  /* contact */
  .contact { position: absolute; left: 468px; top: 1038px; width: 467px; height: 162px; background: var(--grey-panel); border-top-left-radius: 18px; }
  .contact-label { left: 60px; top: 8px; font-family: "Poppins", sans-serif; font-weight: 500; font-size: 19px; }
  .contact-phone { left: 58px; top: 32px; font-family: "Poppins", sans-serif; font-weight: 800; font-size: 41px; color: var(--blue); letter-spacing: 3px; }
  .contact-web, .contact-email { left: 60px; font-family: "Poppins", sans-serif; font-weight: 700; font-size: 16px; letter-spacing: 1.2px; }
  .contact-web { top: 89px; }
  .contact-email { top: 117px; }
  .icon { position: absolute; }
</style>
</head>
<body>
<main class="flyer">

  <div class="abs brand-mark"></div>
  <div class="abs brand-name">TARNWICK</div>
  <div class="abs brand-sub">BATHROOMS</div>

  <h1 class="abs region">ILLAWARRA<span class="region-note">BASED</span></h1>
  <p class="abs family">AND <strong>FAMILY OPERATED</strong></p>

  <div class="abs name-band"><span>TARNWICK BATHROOMS</span></div>
  <p class="abs fully">FULLY</p>
  <p class="abs licensed">LICENSED</p>
  <p class="abs insured"><span class="amp">&amp;</span>INSURED</p>

  <div class="abs hero-photo" role="img" aria-label="Modern bathroom with timber wall panels, marble feature wall, floating vanity and wall-hung toilet"></div>
  <div class="bracket" style="left:453px; top:264px; width:29px; height:369px;"></div>
  <div class="bracket" style="left:453px; top:605px; width:373px; height:28px;"></div>

  <!-- main bathroom package -->
  <div class="save-tab" style="left:0; top:529px; width:360px; border-top-right-radius:10px;"><span style="left:29px;">SAVE UP TO $4,000</span></div>
  <div class="pkg-photo" role="img" aria-label="Main bathroom with glass shower, double vanity and timber-framed mirror" style="left:176px; top:542px; width:247px; height:174px; background:linear-gradient(110deg,#d9dde0,#eeeae6 55%,#b7a79a);"></div>
  <div class="bracket" style="left:416px; top:563px; width:14px; height:160px; border-radius:7px;"></div>
  <div class="bracket" style="left:354px; top:710px; width:76px; height:13px; border-radius:7px;"></div>
  <p class="abs pkg-title" style="left:21px; top:572px; font-size:23px; line-height:30px;">MAIN<br>BATHROOM<br>PACKAGE</p>
  <p class="abs pkg-from" style="left:21px; top:666px;">Price Starts From</p>
  <p class="abs pkg-price" style="left:21px; top:683px;">$18,900</p>

  <!-- ensuite package -->
  <div class="save-tab" style="left:106px; top:746px; width:362px; border-top-left-radius:10px;"><span style="left:194px;">SAVE UP TO $4,000</span></div>
  <div class="pkg-photo" role="img" aria-label="Ensuite vanity with round vessel basin and brushed brass tapware" style="left:42px; top:758px; width:246px; height:175px; background:linear-gradient(120deg,#a9a296,#d9d4cd 50%,#efece8);"></div>
  <div class="bracket" style="left:34px; top:779px; width:15px; height:162px; border-radius:7px;"></div>
  <div class="bracket" style="left:34px; top:927px; width:135px; height:14px; border-radius:7px;"></div>
  <p class="abs pkg-title" style="left:302px; top:797px; font-size:29px; line-height:37px;">ENSUITE<br>PACKAGE</p>
  <p class="abs pkg-from" style="left:302px; top:879px;">Price Starts From</p>
  <p class="abs pkg-price" style="left:302px; top:897px;">$14,900</p>

  <!-- laundry package -->
  <div class="save-tab" style="left:0; top:964px; width:360px; border-top-right-radius:10px;"><span style="left:27px;">SAVE UP TO $4,000</span></div>
  <div class="pkg-photo" role="img" aria-label="Laundry with stacked front-loading washer and dryer under a benchtop sink" style="left:176px; top:977px; width:247px; height:174px; background:linear-gradient(100deg,#cfcfcf,#eae8e5 50%,#e2ddd7);"></div>
  <div class="bracket" style="left:416px; top:998px; width:14px; height:161px; border-radius:7px;"></div>
  <div class="bracket" style="left:354px; top:1146px; width:76px; height:13px; border-radius:7px;"></div>
  <p class="abs pkg-title" style="left:21px; top:1013px; font-size:29px; line-height:37px;">LAUNDRY<br>PACKAGE</p>
  <p class="abs pkg-from" style="left:23px; top:1096px;">Price Starts From</p>
  <p class="abs pkg-price" style="left:22px; top:1113px;">$ 9,900</p>

  <p class="abs terms">*Terms and conditions apply and onsite quote required.</p>

  <!-- services -->
  <section class="services">
    <h2 class="abs services-title">BUILT TO LAST</h2>
    <p class="abs services-sub">Your local renovation specialist</p>
    <ul class="service-list">
      <li>Demolition</li>
      <li>Electrical&nbsp;&nbsp;Carpentry</li>
      <li>Design Consultation</li>
      <li>Waterproofing</li>
      <li>Plumbing</li>
      <li>Tiling</li>
    </ul>
    <p class="abs services-note">Organisation and delivery of all fixtures</p>
  </section>

  <!-- contact -->
  <section class="contact">
    <p class="abs contact-label">Contact Us At</p>
    <p class="abs contact-phone">0487652970</p>
    <p class="abs contact-web">www.tarnwickbathrooms.com.au</p>
    <p class="abs contact-email">Jory@tarnwickbathrooms.com.au</p>
    <svg class="icon" style="left:11px; top:33px;" width="42" height="42" viewBox="0 0 42 42" aria-hidden="true">
      <circle cx="21" cy="21" r="19" fill="none" stroke="#1a6fbd" stroke-width="2.5"/>
      <path d="M14 12c1-1 3-1 4 0l2 3c.5 1 .3 2-.5 2.7l-1.2 1c1 2.2 2.7 4 5 5l1-1.2c.7-.8 1.8-1 2.7-.5l3 2c1 1 1 3 0 4l-1.5 1.5c-6 0-16-10-16-16z" fill="#0d0d0d"/>
    </svg>
    <svg class="icon" style="left:11px; top:89px;" width="42" height="42" viewBox="0 0 42 42" aria-hidden="true">
      <circle cx="21" cy="21" r="19" fill="none" stroke="#1a6fbd" stroke-width="2.5"/>
      <g fill="none" stroke="#0d0d0d" stroke-width="1.8">
        <circle cx="21" cy="21" r="10"/>
        <ellipse cx="21" cy="21" rx="4.5" ry="10"/>
        <line x1="11" y1="21" x2="31" y2="21"/>
        <line x1="12.5" y1="16" x2="29.5" y2="16"/>
        <line x1="12.5" y1="26" x2="29.5" y2="26"/>
      </g>
    </svg>
  </section>

</main>
</body>
</html>
```